Pavewell Summit

Im looking for something similar to (brightcoatpaving.com) web site. I really want it to pop!
services we offer:
- Seal Coating
- Crack Filling
- Striping
- Asphalt
- Concrete
- Signage
- Road Grinding
- Grading
- Hydro Blasting
- Recycled asphalt
- Dumpster Pads
- Pressure Washing
- Wheel blocks
- Bollard installation
- Commercial Curbing
- Job site clean up
- Sweeping
- Forestry Clean up
- ADA Compliant work
- Speed bump installation and removal
- Snow removal
- Custom stair sets (Commercial)
Target Market(s)
Parking lot maintenance, asphalt repairs, road grading
Industry/Entity Type
construction, parking lot maintenance
Coding
Coded - Design and coding required
Number of Pages Required
2 page
Look and feel
Each slider illustrates characteristics of the customer's brand and the style your logo design should communicate.

```html
<!DOCTYPE html>
<html lang="en">
<head>
<meta charset="utf-8">
<title>Pavewell Summit — Paving, Grading &amp; Parking Lot Care</title>
<link href="https://fonts.googleapis.com/css2?family=Montserrat:wght@500;600;700;800;900&family=Open+Sans:wght@400;600&display=swap" rel="stylesheet">
<style>
:root{
  --lime:#86e01e;
  --lime-dark:#5fae0a;
  --ink:#0c0d0c;
  --coal:#151615;
  --asphalt:#1e201f;
  --card:#222423;
  --white:#ffffff;
  --muted:#c9cbc8;
  --grey:#8d918c;
}
*{box-sizing:border-box;margin:0;padding:0}
html,body{width:1200px;height:5212px;overflow:hidden}
body{background:var(--ink);color:var(--white);font-family:"Open Sans",Arial,sans-serif;font-size:13px;line-height:1.6;position:relative}
h1,h2,h3,h4,.brand,.nav a,.btn{font-family:"Montserrat",Arial,sans-serif}
.section{position:absolute;left:0;width:1200px}
.accent{color:var(--lime)}
.title{font-size:30px;font-weight:800;text-align:center;letter-spacing:.5px;text-transform:uppercase}
.title-rule{width:46px;height:4px;background:var(--lime);margin:12px auto 0}
.copy{color:var(--muted);font-size:13px;line-height:1.75}

/* header */
.topbar{top:0;height:72px;background:var(--ink)}
.search{position:absolute;left:128px;top:16px;display:flex;height:40px}
.search span{width:160px;background:#fff;color:#888;font-size:12px;padding:10px 12px}
.search b{width:92px;background:var(--lime);color:#111;font:700 12px "Montserrat",sans-serif;display:flex;align-items:center;justify-content:center}
.brand{position:absolute;left:0;right:0;top:14px;text-align:center;font-size:26px;font-weight:800;letter-spacing:2px;line-height:1.2}
.brand small{display:block;font-size:11px;letter-spacing:6px;font-weight:800}
.socials{position:absolute;left:700px;top:20px;display:flex;gap:10px}
.socials i{width:30px;height:30px;border-radius:50%;background:var(--lime);display:block}
.phone{position:absolute;left:900px;top:12px;text-align:left}
.phone small{display:block;color:var(--lime);font-size:10px;font-weight:600}
.phone strong{font:800 22px "Montserrat",sans-serif}
.navbar{top:72px;height:40px}
.nav{position:absolute;left:128px;width:944px;height:40px;background:var(--lime);display:flex;justify-content:center;align-items:center;gap:38px}
.nav a{color:#0b0b0b;font-size:12px;font-weight:700;text-decoration:none;text-transform:uppercase}

/* hero */
.hero{top:112px;height:628px;background:linear-gradient(180deg,#8aa7bd 0%,#b4b4a4 45%,#7e7360 100%)}
.hero-panel{position:absolute;left:320px;top:150px;width:580px;height:250px;background:rgba(0,0,0,.45);text-align:center;padding-top:40px}
.hero-panel h1{font-size:36px;font-weight:800;text-transform:uppercase}
.hero-panel p{color:#e6e6e6;font-size:12px;width:460px;margin:10px auto 0}
.btn{display:inline-block;border:2px solid var(--lime);color:#fff;font-size:12px;font-weight:700;padding:10px 26px;margin-top:26px;text-transform:uppercase}
.dots{position:absolute;left:0;right:0;top:490px;display:flex;justify-content:center;gap:8px}
.dots i{width:10px;height:10px;border-radius:50%;background:#fff;opacity:.6}
.dots i:first-child{opacity:1}
.hero-edge{position:absolute;left:0;bottom:0}

/* about */
.about{top:740px;height:600px;background:var(--ink)}
.about .ghost{position:absolute;left:0;right:0;top:18px;text-align:center;font:900 130px "Montserrat",sans-serif;color:#fff;opacity:.04;letter-spacing:10px}
.about .title{margin-top:44px;position:relative}
.about .copy{width:800px;margin:30px auto 0;text-align:center}
.project-type{position:absolute;top:260px;width:380px;height:240px}
.project-type .shot{position:absolute;inset:0;clip-path:polygon(6% 0,94% 0,100% 100%,0 100%);border:0}
.project-type .frame{position:absolute;inset:-6px;clip-path:polygon(6% 0,94% 0,100% 100%,0 100%);background:var(--lime);z-index:-1}
.project-type h3{position:absolute;left:0;right:0;bottom:12px;text-align:center;font-size:18px;font-weight:800;text-transform:uppercase}
.commercial{left:200px}.commercial .shot{background:linear-gradient(180deg,#5e86a6,#6f8d4a 55%,#575a57)}
.residential{left:620px}.residential .shot{background:linear-gradient(180deg,#9fc0dd,#6c8f3f 50%,#6e706d)}

/* services */
.services{top:1340px;height:1140px;background:linear-gradient(160deg,#2c2e2d,#161716 60%,#232524)}
.services .title{margin-top:86px}
.service-grid{position:absolute;left:132px;top:160px;width:936px;display:grid;grid-template-columns:repeat(3,300px);gap:40px 18px}
.service{height:420px;background:var(--card);text-align:center;padding:24px 28px 0}
.service.featured{background:var(--lime-dark)}
.service svg{display:block;margin:0 auto}
.service h3{font-size:19px;font-weight:800;text-transform:uppercase;margin-top:20px}
.service p{color:var(--muted);font-size:12px;margin-top:10px}
.service.featured p{color:#eef8e2}
.service a{display:inline-block;color:var(--lime);font:700 11px "Montserrat",sans-serif;text-transform:uppercase;margin-top:14px;border-bottom:1px solid var(--lime)}
.service.featured a{color:#fff;border-color:#fff}

/* promise */
.promise{top:2480px;height:460px;background:var(--ink)}
.promise .shot{position:absolute;left:140px;top:112px;width:380px;height:320px;background:linear-gradient(180deg,#7ea0b8,#6d6b48 55%,#3c3b36);clip-path:polygon(50% 0,100% 100%,68% 100%,50% 62%,32% 100%,0 100%)}
.promise h2{position:absolute;left:600px;top:110px;font-size:28px;font-weight:800;text-transform:uppercase}
.promise .rule{position:absolute;left:600px;top:160px;width:46px;height:4px;background:var(--lime)}
.promise .copy{position:absolute;left:600px;top:184px;width:480px}

/* clients */
.clients{top:2940px;height:340px;background:linear-gradient(180deg,#1a1b1a,#2a2c2b 50%,#171817)}
.clients .title{margin-top:176px}
.client-row{position:absolute;left:128px;top:258px;width:944px;display:flex;gap:16px}
.client{flex:1;height:62px;background:#fff;color:#222;display:flex;align-items:center;justify-content:center;gap:6px;font:700 12px "Montserrat",sans-serif}
.client i{width:10px;height:10px;background:var(--lime-dark);display:block}
.arrow{position:absolute;top:270px}

/* gallery */
.gallery{top:3280px;height:760px;background:var(--ink)}
.gallery .title{margin-top:136px}
.gallery-grid{position:absolute;left:140px;top:240px;width:920px;display:grid;grid-template-columns:repeat(4,1fr);grid-template-rows:236px 236px;gap:8px}
.gallery-grid div{position:relative}
.g1{background:linear-gradient(180deg,#6f98b9,#4b7a3a 50%,#7d7f7b)}
.g2{background:linear-gradient(180deg,#6b6c66,#c8a436 60%,#5e5e58)}
.g3{background:linear-gradient(180deg,#5d7c94,#85887e 60%,#3f403c)}
.g4{background:linear-gradient(180deg,#6f9fca,#3f5f37 55%,#6e6f6c)}
.g5{background:linear-gradient(180deg,#9a9a94,#d9c21e 60%,#7b7a74)}
.g6{background:linear-gradient(180deg,#7d7d78,#c25c3f 55%,#9a7b63)}
.g7{background:linear-gradient(180deg,#8d8d88,#c6a52d 55%,#6b6b66)}
.g8{background:linear-gradient(180deg,#a28476,#b9533d 55%,#8c4636)}
.play{position:absolute;left:50%;top:50%;transform:translate(-50%,-50%)}

/* contact */
.contact{top:4040px;height:520px;background:linear-gradient(180deg,#4a5a66 0%,#5d5640 45%,#2a2a25 100%)}
.contact .title{margin-top:96px}
.contact-form{position:absolute;left:240px;top:180px;width:720px;display:grid;grid-template-columns:1fr 1fr;gap:16px 16px}
.field{height:40px;background:#fff;color:#777;font-size:12px;padding:10px 12px}
.field.wide{grid-column:1/3;height:100px}
.submit{position:absolute;left:525px;top:468px;width:150px;height:36px;background:var(--ink);border:2px solid var(--lime);font:700 12px "Montserrat",sans-serif;display:flex;align-items:center;justify-content:center;text-transform:uppercase}

/* newsletter + footer */
.newsletter{top:4560px;height:320px;background:linear-gradient(180deg,#1d1e1c,#0f100f)}
.wordmark{position:absolute;left:0;right:0;top:24px;text-align:center;font:900 150px "Montserrat",sans-serif;color:var(--lime);letter-spacing:6px;line-height:1}
.newsletter h2{position:absolute;left:0;right:0;top:212px;text-align:center;font-size:24px;font-weight:800;text-transform:uppercase}
.subscribe{position:absolute;left:420px;top:260px;display:flex;height:40px}
.subscribe span{width:344px;background:#fff;color:#888;font-size:12px;padding:10px 14px}
.subscribe b{width:116px;background:var(--lime);color:#111;font:700 12px "Montserrat",sans-serif;display:flex;align-items:center;justify-content:center;text-transform:uppercase}
.footer{top:4880px;height:332px;background:var(--ink)}
.footer .line{position:absolute;left:120px;width:960px;top:0;height:1px;background:#333}
.footer .brand{left:120px;right:auto;top:80px;text-align:left;font-size:30px}
.footer .socials{left:120px;top:150px}
.footer .socials i{width:24px;height:24px}
.fcol{position:absolute;top:40px}
.fcol h4{font-size:14px;font-weight:800;text-transform:uppercase;margin-bottom:10px}
.fcol li{list-style:none;color:var(--muted);font-size:12px;line-height:1.9;padding-left:14px;position:relative}
.fcol li::before{content:"";position:absolute;left:0;top:9px;width:5px;height:5px;background:var(--lime)}
.q{left:400px}.l{left:640px}.c{left:840px;width:240px}
.bottom{position:absolute;left:120px;width:960px;top:258px;border-top:1px solid #333;padding-top:14px;display:flex;justify-content:space-between;color:var(--grey);font-size:11px}
.cards{display:flex;gap:6px}
.cards i{width:34px;height:20px;background:#e8e8e8;border-radius:3px;display:block}
</style>
</head>
<body>

<header class="section topbar">
  <div class="search"><span>Search here</span><b>SEARCH</b></div>
  <div class="brand">PAVEWELL<small>SUMMIT</small></div>
  <div class="socials"><i></i><i></i><i></i><i></i></div>
  <div class="phone"><small>CALL US FOR A FREE ESTIMATE</small><strong>+1 (555) 014-2287</strong></div>
</header>
<nav class="section navbar">
  <div class="nav"><a>Home</a><a>Services</a><a>Gallery</a><a>Leave a Review</a><a>About Us</a><a>Contact Us</a></div>
</nav>

<section class="section hero" role="img" aria-label="Compact track loader grading a gravel lot under a cloudy sky">
  <div class="hero-panel">
    <h1>Welcome to <span class="accent">Pavewell Summit</span></h1>
    <p>Paving, grading and lot care done right, on time and on budget for every commercial and residential site.</p>
    <span class="btn">Get Started</span>
  </div>
  <div class="dots"><i></i><i></i><i></i><i></i></div>
  <svg class="hero-edge" width="1200" height="70" viewBox="0 0 1200 70">
    <path d="M0 20 Q600 75 1200 20 L1200 70 L0 70Z" fill="#0c0d0c"/>
    <path d="M0 20 Q600 75 1200 20" fill="none" stroke="#86e01e" stroke-width="6"/>
  </svg>
</section>

<section class="section about">
  <div class="ghost">PAVEWELL</div>
  <h2 class="title">About Pavewell Summit</h2>
  <div class="title-rule"></div>
  <p class="copy">Pavewell Summit is a local team of paving and site crews serving parking lots, roads and driveways across the region. We handle seal coating, crack filling, striping, grading, grinding and sweeping with modern equipment and careful planning. Every job starts with a clear estimate and ends with a clean site, so owners and managers can count on a smooth, safe surface that lasts for years to come.</p>
  <div class="project-type commercial"><div class="frame"></div><div class="shot" role="img" aria-label="Commercial parking lot lined with trees"></div><h3>Commercial</h3></div>
  <div class="project-type residential"><div class="frame"></div><div class="shot" role="img" aria-label="Freshly paved residential street"></div><h3>Residential</h3></div>
</section>

<section class="section services" role="img" aria-label="Dark asphalt surface with faded road markings">
  <h2 class="title">Services <span class="accent">We Offer</span></h2>
  <div class="title-rule"></div>
  <div class="service-grid">
    <article class="service">
      <svg width="96" height="96" viewBox="0 0 96 96"><rect x="20" y="20" width="56" height="56" transform="rotate(45 48 48)" fill="#86e01e" stroke="#0c0d0c" stroke-width="3"/><path d="M38 66 Q58 48 40 32 L56 30" fill="none" stroke="#0c0d0c" stroke-width="5"/></svg>
      <h3>Road Grading</h3>
      <p>We level and shape gravel and dirt roads so water drains away and the surface stays firm, smooth and safe through every season of the year.</p>
      <a>Learn More</a>
    </article>
    <article class="service featured">
      <svg width="96" height="96" viewBox="0 0 96 96"><rect x="20" y="20" width="56" height="56" transform="rotate(45 48 48)" fill="#86e01e" stroke="#0c0d0c" stroke-width="3"/><rect x="32" y="42" width="32" height="14" fill="#0c0d0c"/><circle cx="38" cy="60" r="5" fill="#0c0d0c"/><circle cx="58" cy="60" r="5" fill="#0c0d0c"/></svg>
      <h3>Asphalt Grinding</h3>
      <p>Worn asphalt is milled down and removed to prepare a clean base for new pavement, saving material and keeping grades right at curbs and drains.</p>
      <a>Learn More</a>
    </article>
    <article class="service">
      <svg width="96" height="96" viewBox="0 0 96 96"><rect x="20" y="20" width="56" height="56" transform="rotate(45 48 48)" fill="#86e01e" stroke="#0c0d0c" stroke-width="3"/><circle cx="48" cy="48" r="14" fill="none" stroke="#0c0d0c" stroke-width="4"/><path d="M38 40 L58 56 M58 40 L38 56" stroke="#0c0d0c" stroke-width="3"/></svg>
      <h3>Street Sweeping</h3>
      <p>Scheduled sweeping keeps lots and streets free of debris, dust and grit, protecting the pavement and giving visitors a clean first impression.</p>
      <a>Learn More</a>
    </article>
    <article class="service">
      <svg width="96" height="96" viewBox="0 0 96 96"><rect x="20" y="20" width="56" height="56" transform="rotate(45 48 48)" fill="#86e01e" stroke="#0c0d0c" stroke-width="3"/><rect x="30" y="44" width="30" height="12" fill="#0c0d0c"/><path d="M60 50 L68 58 L60 58Z" fill="#0c0d0c"/><circle cx="38" cy="60" r="4" fill="#0c0d0c"/><circle cx="52" cy="60" r="4" fill="#0c0d0c"/></svg>
      <h3>Grading</h3>
      <p>Site grading sets the right slope for drainage and paving, building a stable and well compacted base before any asphalt or concrete goes down.</p>
      <a>Learn More</a>
    </article>
    <article class="service">
      <svg width="96" height="96" viewBox="0 0 96 96"><rect x="20" y="20" width="56" height="56" transform="rotate(45 48 48)" fill="#86e01e" stroke="#0c0d0c" stroke-width="3"/><path d="M34 58 L48 34 L62 58Z" fill="none" stroke="#0c0d0c" stroke-width="4"/><circle cx="48" cy="50" r="4" fill="#0c0d0c"/></svg>
      <h3>Asphalt Coloring</h3>
      <p>Colored coatings mark walkways, crossings and bike lanes, adding safety and curb appeal to plazas, schools and busy commercial entrances.</p>
      <a>Learn More</a>
    </article>
    <article class="service">
      <svg width="96" height="96" viewBox="0 0 96 96"><rect x="20" y="20" width="56" height="56" transform="rotate(45 48 48)" fill="#86e01e" stroke="#0c0d0c" stroke-width="3"/><path d="M40 32 V64 M56 32 V64 M48 34 V42 M48 48 V56" stroke="#0c0d0c" stroke-width="4"/></svg>
      <h3>Asphalt Patching</h3>
      <p>Potholes and broken areas are cut out and patched with hot mix, restoring a smooth surface and stopping water from spreading the damage.</p>
      <a>Learn More</a>
    </article>
  </div>
</section>

<section class="section promise">
  <div class="shot" role="img" aria-label="Paving crew at work on a road, framed in a triangular shape"></div>
  <h2>Our Customer <span class="accent">Promise</span></h2>
  <div class="rule"></div>
  <p class="copy">We show up when we say we will, explain every step and stand behind our work. Our crews protect your property, keep traffic moving and leave the site cleaner than we found it. From a single pothole to a full lot rebuild, you get honest pricing, quality materials and a finish you can be proud of. We treat each project as if it were our own, with clear updates from the first call to the final walkthrough, and we follow up after the job to make sure the results still meet your needs season after season.</p>
</section>

<section class="section clients" role="img" aria-label="Dark textured background">
  <h2 class="title">Some of <span class="accent">Our Clients</span></h2>
  <svg class="arrow" style="left:76px" width="24" height="36" viewBox="0 0 24 36"><path d="M20 4 L6 18 L20 32" fill="none" stroke="#fff" stroke-width="4"/></svg>
  <div class="client-row">
    <div class="client"><i></i>Ridgeline Lots</div>
    <div class="client"><i></i>Northpass Road</div>
    <div class="client"><i></i>Cedar Yard</div>
    <div class="client"><i></i>Harbor Build</div>
    <div class="client"><i></i>Summit Star</div>
    <div class="client"><i></i>Granite Co</div>
  </div>
  <svg class="arrow" style="left:1100px" width="24" height="36" viewBox="0 0 24 36"><path d="M4 4 L18 18 L4 32" fill="none" stroke="#fff" stroke-width="4"/></svg>
</section>

<section class="section gallery">
  <h2 class="title">Our Project <span class="accent">Gallery</span></h2>
  <div class="gallery-grid">
    <div class="g1" role="img" aria-label="Paved path through a green park"></div>
    <div class="g2" role="img" aria-label="Yellow parking stop on asphalt"></div>
    <div class="g3" role="img" aria-label="Crew working on a road at dusk"><svg class="play" width="44" height="44" viewBox="0 0 44 44"><circle cx="22" cy="22" r="22" fill="#86e01e"/><path d="M17 13 L31 22 L17 31Z" fill="#0c0d0c"/></svg></div>
    <div class="g4" role="img" aria-label="Driveway beside a lawn and trees"></div>
    <div class="g5" role="img" aria-label="Yellow bollards in a parking garage"></div>
    <div class="g6" role="img" aria-label="Red colored asphalt walkway"></div>
    <div class="g7" role="img" aria-label="Bollards lining a loading area"></div>
    <div class="g8" role="img" aria-label="Red brick pattern pavement"></div>
  </div>
</section>

<section class="section contact" role="img" aria-label="Track loader working in a field at the edge of a cornfield">
  <h2 class="title">Get in <span class="accent">Touch</span></h2>
  <div class="contact-form">
    <div class="field">First Name</div>
    <div class="field">Last Name</div>
    <div class="field">Email</div>
    <div class="field">Phone</div>
    <div class="field wide">How Can We Help?</div>
  </div>
  <div class="submit">Submit</div>
</section>

<section class="section newsletter">
  <div class="wordmark">PAVEWELL</div>
  <h2>Join Our Mailing List</h2>
  <div class="subscribe"><span>Enter Email Here</span><b>Subscribe</b></div>
</section>

<footer class="section footer">
  <div class="line"></div>
  <div class="brand">PAVEWELL<small>SUMMIT</small></div>
  <div class="socials"><i></i><i></i><i></i><i></i></div>
  <div class="fcol q"><h4>Quick Links</h4><ul><li>Home</li><li>About</li><li>Services</li><li>Blog</li></ul></div>
  <div class="fcol l"><h4>Legal</h4><ul><li>Privacy Policy</li><li>Terms &amp; Conditions</li><li>Contact Us</li><li>Cookie Policy</li></ul></div>
  <div class="fcol c"><h4>Contact Us</h4><ul><li>1427 Quarry Lane, Suite 8, Ridgefield</li><li>+1 (555) 014-2287</li><li>hello@pavewellsummit.com</li></ul></div>
  <div class="bottom"><span>© Copyright 2021 Pavewell Summit | All Rights Reserved</span><span class="cards"><i></i><i></i><i></i><i></i></span></div>
</footer>

</body>
</html>
```